WP website design Pardo-Kettleby(Contest)

We need a wordpress design that will incorporate a professional color scheme with company logo in a clean layout. The design needs to consider that this will be developed on a responsive theme. Colors are blue and green of the logo and and an accent color (perhaps very light brown/tan). Client wants a 'modern' look.

Industry/Entity Type

It Company

Font styles to use
Serif
Sans Serif

Colors

Designer to choose colors to be used in the design.

Requirements
Must have
• navigation: 1) Home; 2) Services; 3) Auctions by Type; 4) About Us; 5) VQL Digest 6) Videos; 7) Contact Us

VERY general idea of layout is attached, Site will have slideshow, image is attached. Widgets used to are: 1) Email Contact Form; 2) social media icons, FB LinedIn, ClipStream; 3) Featured Auctions; 4) News & Events blog; Featured Video

Footer will have affiliation logos, contact info and perhaps smaller company logo:
Phone: (555) 304-7192 / Mobile: (555) 618-2047 (Mirna)
Email: mkettleby417@postvale.example / dennis@pardokettleby.example
Address: 415 FM 733N • #B207 • PMB318 • Austin, TX 78690

Nice to have
• Use of a dropdown menu

```html
<!DOCTYPE html>
<html lang="en">
<head>
<meta charset="utf-8">
<title>Pardo-Kettleby Auction Marketing</title>
<link href="https://fonts.googleapis.com/css2?family=Open+Sans:wdth,wght@75..100,400..700&family=Pathway+Gothic+One&display=swap" rel="stylesheet">
<style>
:root{
  --navy:#0b3d7a;
  --blue:#1467b8;
  --blue-dark:#0c55a0;
  --title:#1a8fd0;
  --cyan:#2fb6c8;
  --green:#7cb82f;
  --text:#555;
  --footer:#0a5aa3;
  --field:#fff;
}
*{margin:0;padding:0;box-sizing:border-box}
html,body{width:678px;height:1200px;overflow:hidden}
body{position:relative;font-family:"Open Sans",Arial,sans-serif;color:var(--text);background:#fff}
.abs{position:absolute}
.header{left:0;top:0;width:678px;height:98px;background:linear-gradient(#f2f4f6,#e3e7ea)}
.brand{left:84px;top:18px;width:130px;color:var(--navy);font-weight:700;font-size:14px;line-height:16px;text-align:center}
.brand .dot{display:inline-block;width:12px;height:12px;border-radius:50%;background:var(--green);margin-bottom:4px}
.help{right:114px;top:29px;font-size:8px;line-height:11px;color:#333;text-align:left;white-space:nowrap}
.phone-ico{left:570px;top:22px}
.phone-num{left:481px;top:56px;font-size:20px;color:#111;white-space:nowrap}
.nav{left:0;top:98px;width:678px;height:24px;background:linear-gradient(#2a82d1,#1261b0)}
.nav a{position:absolute;top:0;height:24px;line-height:24px;color:#fff;font-size:8.5px;font-weight:700;text-decoration:none;text-align:center;white-space:nowrap;border-right:1px solid rgba(0,0,0,.15)}
.nav a.active{background:linear-gradient(#4fc0ee,#2a9ad8)}
.nav a.open{background:var(--blue-dark)}
.dropdown{left:134px;top:122px;width:111px;height:72px;background:var(--blue-dark);z-index:3;padding:4px 0 0 17px}
.dropdown li{list-style:none;color:#fff;font-size:8.5px;line-height:16.5px}
.hero{left:0;top:122px;width:678px;height:284px;background:linear-gradient(135deg,#a8b5ad 0%,#6f9484 35%,#8aa79a 55%,#c5c9c2 80%,#8c9792 100%)}
.hero-title{left:0;width:678px;text-align:center;font-family:"Pathway Gothic One",sans-serif;color:#111;letter-spacing:1px;white-space:nowrap;line-height:1}
.btn-more{left:293px;top:348px;width:91px;height:24px;background:var(--green);color:#fff;font-size:9px;font-weight:700;text-align:center;line-height:24px}
.videos{left:0;top:406px;width:678px;height:86px;background:linear-gradient(#fff,#cfe6f6)}
.video{top:414px;width:80px}
.video h4{font-size:8.5px;color:var(--navy);font-weight:600;margin-bottom:5px;white-space:nowrap}
.video .thumb{width:80px;height:51px;background:#000;border:3px solid #1a6fc0;display:flex;align-items:center;justify-content:center}
h2.section{font-size:16px;font-weight:400;color:var(--navy);white-space:nowrap;line-height:1.2}
h2.section span{color:var(--title)}
h2.welcome{font-size:14.5px;font-stretch:82%;width:360px;overflow:hidden}
.copy{font-size:7px;line-height:11px;color:#666}
.upcoming{left:74px;top:601px;width:350px;height:106px;border:2px solid var(--blue)}
.up-art{left:0;top:0;width:176px;height:84px;background:linear-gradient(90deg,#eef3f7,#dfe7ee)}
.up-label{left:0;top:28px;width:118px;height:38px;background:var(--blue);color:#fff;font-size:14px;line-height:17px;padding:2px 6px;font-weight:600}
.up-bar{left:0;top:84px;width:346px;height:18px;background:var(--blue);color:#fff;font-size:8.5px;font-weight:700;text-align:right;padding-right:14px;line-height:18px;letter-spacing:.5px}
.feat{top:768px;width:100px;text-align:center;font-size:7.5px;color:#444}
.feat svg{display:block;margin:0 auto 8px}
.partner{top:970px;width:78px;height:50px;border:1px solid #ddd;background:#fff;display:flex;align-items:center;justify-content:center}
.partner i{display:block;background:#333}
.form{left:444px;top:511px;width:160px;height:257px;background:#f0f0f0}
.form-head{height:30px;background:linear-gradient(#46c8ee,#1ea0d8);color:#fff;font-size:14px;font-weight:600;line-height:30px;padding-left:12px}
.field{left:12px;width:136px;height:19px;background:var(--field);border:1px solid #ccc;font-size:7px;color:#444;padding:4px 6px}
.captcha{left:85px;top:196px;width:35px;height:19px;background:#000;color:#fff;font-size:8px;font-weight:700;text-align:center;line-height:19px}
.submit{left:10px;top:224px;width:55px;height:23px;background:linear-gradient(#4ccaf0,#1a9ad6);color:#fff;font-size:9px;font-weight:700;text-align:center;line-height:23px}
.news-img{left:444px;width:48px;height:50px;background:linear-gradient(135deg,#8b9b93,#5f7d70,#b4b9b3)}
.news-text{left:500px;width:106px;font-size:7.5px;line-height:11.5px;color:#555}
.readmore{left:553px;width:51px;height:14px;background:#eee;font-size:7.5px;text-align:center;line-height:14px;color:#333}
.footer{left:0;top:1050px;width:678px;height:126px;background:var(--footer);color:#fff}
.footer h5{font-size:10.5px;font-weight:700;letter-spacing:.3px}
.footer p{font-size:7.5px;line-height:11px;color:#d7e6f5;white-space:nowrap}
.social{left:502px;font-size:7.5px;color:#d7e6f5;display:flex;align-items:center;gap:8px}
.social b{display:block;width:18px;height:18px;background:#2fa6d9}
.copyright{left:0;top:1176px;width:678px;height:24px;background:var(--cyan);color:#fff;font-size:7.5px;text-align:center;line-height:24px}
</style>
</head>
<body>

<header class="abs header">
  <div class="abs brand"><span class="dot"></span><br>Pardo-Kettleby<br>Auction Marketing</div>
  <div class="abs help">Need help from us?<br>Feel free to call us</div>
  <svg class="abs phone-ico" width="34" height="34" viewBox="0 0 34 34" aria-hidden="true">
    <rect x="2" y="2" width="9" height="30" rx="3" fill="#1f6fc0"/>
    <rect x="12" y="6" width="20" height="24" rx="3" fill="#1f6fc0"/>
    <g fill="#fff"><rect x="15" y="9" width="14" height="5"/><rect x="15" y="17" width="3" height="3"/><rect x="20.5" y="17" width="3" height="3"/><rect x="26" y="17" width="3" height="3"/><rect x="15" y="23" width="3" height="3"/><rect x="20.5" y="23" width="3" height="3"/><rect x="26" y="23" width="3" height="3"/></g>
  </svg>
  <div class="abs phone-num">1-800-555-0143</div>
</header>

<nav class="abs nav">
  <a class="active" href="#" style="left:74px;width:60px">HOME</a>
  <a class="open" href="#" style="left:134px;width:75px">SERVICES</a>
  <a href="#" style="left:209px;width:113px">AUCTIONS BY TYPE</a>
  <a href="#" style="left:322px;width:73px">ABOUT US</a>
  <a href="#" style="left:395px;width:79px">VQL DIGEST</a>
  <a href="#" style="left:474px;width:60px">VIDEOS</a>
  <a href="#" style="left:534px;width:84px;border-right:0">CONTACT US</a>
</nav>
<ul class="abs dropdown"><li>Service 1</li><li>Service 2</li><li>Service 3</li><li>Service 4</li></ul>

<section class="abs hero" role="img" aria-label="Slideshow photo of a factory floor with green industrial machinery"></section>
<div class="abs hero-title" style="top:208px;font-size:46px">MAKING “SOLD”</div>
<div class="abs hero-title" style="top:276px;font-size:46px">OUR SPECIALITY FOR 30 YEARS</div>
<div class="abs btn-more">LEARN MORE »</div>

<section class="abs videos"></section>
<div class="abs video" style="left:74px"><h4>PRAESENTIUM</h4><div class="thumb"><svg width="14" height="14" viewBox="0 0 14 14"><circle cx="7" cy="7" r="6" fill="none" stroke="#888"/><path d="M5.5 4.5l4 2.5-4 2.5z" fill="#888"/></svg></div></div>
<div class="abs video" style="left:164px"><h4>DUCIMUS QUI</h4><div class="thumb"><svg width="14" height="14" viewBox="0 0 14 14"><circle cx="7" cy="7" r="6" fill="none" stroke="#888"/><path d="M5.5 4.5l4 2.5-4 2.5z" fill="#888"/></svg></div></div>
<div class="abs video" style="left:254px"><h4>OCCAECATI CUPI</h4><div class="thumb"><svg width="14" height="14" viewBox="0 0 14 14"><circle cx="7" cy="7" r="6" fill="none" stroke="#888"/><path d="M5.5 4.5l4 2.5-4 2.5z" fill="#888"/></svg></div></div>
<div class="abs video" style="left:344px"><h4>NAM LIBERO</h4><div class="thumb"><svg width="14" height="14" viewBox="0 0 14 14"><circle cx="7" cy="7" r="6" fill="none" stroke="#888"/><path d="M5.5 4.5l4 2.5-4 2.5z" fill="#888"/></svg></div></div>
<div class="abs video" style="left:434px"><h4>ELIGENDI OPTIO</h4><div class="thumb"><svg width="14" height="14" viewBox="0 0 14 14"><circle cx="7" cy="7" r="6" fill="none" stroke="#888"/><path d="M5.5 4.5l4 2.5-4 2.5z" fill="#888"/></svg></div></div>
<div class="abs video" style="left:524px"><h4>DOLORUM FUGA</h4><div class="thumb"><svg width="14" height="14" viewBox="0 0 14 14"><circle cx="7" cy="7" r="6" fill="none" stroke="#888"/><path d="M5.5 4.5l4 2.5-4 2.5z" fill="#888"/></svg></div></div>

<h2 class="abs section welcome" style="left:74px;top:506px"><span>WELCOME</span> PARDO-KETTLEBY AUCTION MARKETING</h2>
<p class="abs copy" style="left:74px;top:531px;width:352px">Sed ut perspiciatis unde omnis iste natus error sit voluptatem accusantium doloremque laudantium, totam rem aperiam, eaque ipsa quae ab illo inventore veritatis et quasi architecto beatae vitae dicta sunt explicabo. Nemo enim ipsam voluptatem quia voluptas sit aspernatur aut odit aut fugit, sed quia consequuntur magni dolores eos qui ratione voluptatem sequi nesciunt. sed quia non numquam eius modi tempora incidunt ut labore et dolore magnam aliquam quaerat voluptatem.</p>

<div class="abs upcoming">
  <div class="abs up-art" role="img" aria-label="Illustration of a wall clock and a calendar"></div>
  <div class="abs up-label">UPCOMING<br>AUCTIONS</div>
  <p class="abs copy" style="left:186px;top:12px;width:152px">At vero eos et accusamus et iusto odio dignissimos ducimus qui blanditiis praesentium voluptatum deleniti atque corrupti quos dolores et quas molestias excepturi sint occaecati cupiditate non.</p>
  <div class="abs up-bar">MORE AUCTIONS »</div>
</div>

<h2 class="abs section" style="left:74px;top:726px"><span>FEATURED</span> AUCTIONS</h2>
<div class="abs feat" style="left:59px;color:var(--title)"><svg width="36" height="36" viewBox="0 0 36 36"><path d="M18 4L3 18h5v14h8v-9h4v9h8V18h5z" fill="#1a9ad6"/></svg>Real Estate</div>
<div class="abs feat" style="left:140px"><svg width="44" height="36" viewBox="0 0 44 36"><g fill="#aaa"><rect x="4" y="12" width="3" height="18"/><rect x="10" y="8" width="3" height="22"/><rect x="16" y="10" width="3" height="20"/><rect x="22" y="6" width="3" height="24"/><rect x="28" y="10" width="3" height="20"/><rect x="34" y="12" width="3" height="18"/><rect x="2" y="30" width="38" height="3"/></g></svg>Business Liquidations</div>
<div class="abs feat" style="left:239px"><svg width="36" height="36" viewBox="0 0 36 36"><rect x="9" y="3" width="18" height="31" fill="#aaa"/><g fill="#fff"><rect x="12" y="7" width="4" height="4"/><rect x="20" y="7" width="4" height="4"/><rect x="12" y="14" width="4" height="4"/><rect x="20" y="14" width="4" height="4"/><rect x="12" y="21" width="4" height="4"/><rect x="20" y="21" width="4" height="4"/><rect x="16" y="28" width="4" height="6"/></g></svg>Commercial, Industrial<br>&amp; Specialty Assets</div>
<div class="abs feat" style="left:324px"><svg width="36" height="36" viewBox="0 0 36 36"><path d="M12 20l-4 14 6-3 4 4 2-13zM24 20l4 14-6-3-4 4-2-13z" fill="#aaa"/><circle cx="18" cy="13" r="10" fill="#aaa"/><path d="M18 7l1.8 3.8 4 .5-3 2.8.8 4L18 16l-3.6 2 .8-4-3-2.8 4-.5z" fill="#fff"/></svg>Appraisals</div>
<p class="abs copy" style="left:74px;top:864px;width:352px">provident, similique sunt in culpa qui officia deserunt mollitia animi, id est laborum et dolorum fuga. Et harum quidem rerum facilis est et expedita distinctio. Nam libero tempore, cum soluta nobis est eligendi optio cumque nihil impedit quo minus id quod maxime placeat facere possimus.</p>

<h2 class="abs section" style="left:74px;top:932px"><span>OUR</span> PARTNERS</h2>
<div class="abs" style="left:74px;top:956px;width:350px;height:1px;background:#ddd"></div>
<div class="abs partner" style="left:74px"><i style="width:32px;height:32px;border-radius:50%"></i></div>
<div class="abs partner" style="left:164px"><i style="width:24px;height:30px;border-radius:3px"></i></div>
<div class="abs partner" style="left:254px"><i style="width:28px;height:28px"></i></div>
<div class="abs partner" style="left:344px"><i style="width:56px;height:22px"></i></div>

<aside class="abs form">
  <div class="form-head">CONTACT FORM</div>
  <div class="abs field" style="top:42px">Enter Your Name :</div>
  <div class="abs field" style="top:72px">Enter Your Email :</div>
  <div class="abs field" style="top:102px">Enter Your Phone No. :</div>
  <div class="abs field" style="top:130px;height:56px">Enter Your Message :</div>
  <div class="abs field" style="top:196px;width:68px">Enter Code :</div>
  <div class="abs captcha">xWuab</div>
  <div class="abs submit">SUBMIT</div>
</aside>

<h2 class="abs section" style="left:444px;top:783px;font-size:16px">NEWS &amp; EVENTS</h2>
<div class="abs" style="left:444px;top:805px;width:160px;height:1px;background:#ccc"></div>
<div class="abs news-img" style="top:821px" role="img" aria-label="News photo of industrial machinery"></div>
<p class="abs news-text" style="top:820px">voluptatum deleniti atque corrupti quos dolores et quas molestias excepturi sint occaecati cupiditate non provident, similique sunt .</p>
<div class="abs readmore" style="top:886px">Read More...</div>
<div class="abs news-img" style="top:925px" role="img" aria-label="News photo of industrial machinery"></div>
<p class="abs news-text" style="top:923px">voluptatum deleniti atque corrupti quos dolores et quas molestias excepturi sint occaecati cupiditate non provident, similique sunt .</p>
<div class="abs readmore" style="top:994px">Read More...</div>

<footer class="abs footer">
  <div class="abs" style="left:74px;top:22px;width:130px;color:#fff;font-weight:700;font-size:14px;line-height:16px;text-align:center">Pardo-Kettleby<br>Auction Marketing</div>
  <h5 class="abs" style="left:228px;top:16px">CONTACT DETAILS</h5>
  <p class="abs" style="left:228px;top:40px">415 FM 733N • #B207 • PMB318<br>• Austin, TX 78690</p>
  <p class="abs" style="left:228px;top:72px">Phone :<br>(555) 304-7192<br>(555) 618-2047 (Mirna)</p>
  <p class="abs" style="left:360px;top:48px">Email :<br>mkettleby417@postvale.example<br>dennis@pardokettleby.example</p>
  <h5 class="abs" style="left:502px;top:16px">STAY CONNECTED</h5>
  <div class="abs social" style="top:40px"><b></b>Follow us on Chatterly</div>
  <div class="abs social" style="top:66px"><b></b>Follow us on WorkLink</div>
  <div class="abs social" style="top:93px"><b></b>Follow us on ClipStream</div>
</footer>
<div class="abs copyright">Copyright ©2014 Pardo-Kettleby Auction Marketing</div>

</body>
</html>
```